Tolvern Business Cards

Business card design. dont mind if new logo is suggested.
it would be for a security company.
our clients would be bigger security companies around Australia.
have a logo done but can be replaced. see attaached. like the colors.
Need company name, person name, designation, phone and email on front.
At back company logo and name. website saddress and 2 x license numbers
would like to have 2 different background color for both sidde

Industry/Entity Type

Security

Contact Information for Business Card

round corners, front should be light in color. need logo at back with webaddress and 2 x license numners

Font styles to use
Sans Serif

Colors
f37122
faa54b
f8ba93
0255a3
0592cd
85cae6
b3d448
9bcb3c
ffffff

Requirements
Must have
• see description
Nice to have
• see description
Should not have
• should not be difficult to read or hardd to find information on card.. lets say easy on eyes yet catchy

```html
<!DOCTYPE html>
<html lang="en">
<head>
<meta charset="utf-8">
<title>Tolvern Security Group – Business Card Front</title>
<link rel="stylesheet" href="https://fonts.googleapis.com/css2?family=Arimo:wght@400;700&display=swap">
<style>
  :root {
    --card-bg: #ffffff;
    --ink-band: #1e1e1e;
    --brand-blue: #0255a3;
    --on-band: #ffffff;
    --dot-sky: #cde8f5;
    --dot-steel: #c6d9ea;
  }
  * { margin: 0; padding: 0; box-sizing: border-box; }
  html, body {
    width: 1200px;
    height: 800px;
    overflow: hidden;
    background: var(--card-bg);
  }
  .card {
    position: relative;
    width: 1200px;
    height: 800px;
    background: var(--card-bg);
    font-family: "Arimo", "Helvetica Neue", Arial, sans-serif;
    overflow: hidden;
  }
  .dot-field {
    position: absolute;
    left: 410px;
    top: 16px;
    width: 760px;
    height: 760px;
    border-radius: 50%;
    background: radial-gradient(circle at 50% 50%,
      rgba(255,255,255,0) 0%,
      var(--dot-sky) 30%,
      var(--dot-steel) 58%,
      rgba(198,217,234,0.55) 78%,
      rgba(255,255,255,0) 100%);
  }
  .rule {
    position: absolute;
    left: 0;
    width: 777px;
    height: 7px;
    background: var(--ink-band);
  }
  .rule--top { top: 277px; }
  .rule--bottom { top: 501px; }
  .name-band {
    position: absolute;
    left: 0;
    top: 296px;
    width: 777px;
    height: 195px;
    background: var(--ink-band);
  }
  .text {
    position: absolute;
    left: 47px;
    line-height: 1;
    white-space: nowrap;
  }
  .company {
    top: 242px;
    font-size: 29px;
    color: var(--brand-blue);
    letter-spacing: 0.2px;
  }
  .person-name {
    left: 45px;
    top: 298px;
    font-size: 120px;
    font-weight: 700;
    color: var(--on-band);
    letter-spacing: -1px;
  }
  .role {
    left: 49px;
    top: 416px;
    font-size: 48px;
    color: var(--on-band);
  }
  .email, .phone {
    font-size: 40px;
    color: var(--brand-blue);
  }
  .email { top: 517px; }
  .phone { top: 569px; letter-spacing: 1px; }
</style>
</head>
<body>
  <main class="card">
    <div class="dot-field" role="img" aria-label="Radiating pattern of soft light-blue circles"></div>

    <p class="text company">TOLVERN SECURITY GROUP</p>

    <div class="rule rule--top"></div>
    <div class="name-band"></div>
    <div class="rule rule--bottom"></div>

    <h1 class="text person-name">John Doe</h1>
    <p class="text role">Director</p>

    <p class="text email">jordan@tolvernsecurity.com.au</p>
    <p class="text phone">0491 570 156</p>
  </main>
</body>
</html>
```